Hispanic Financial Counseling and Advocate Firm seeks business card design

Looking for a clean, professional business card design. This is a firm that specializes in providing financial education, coaching, and planning to the Hispanic community. The name of the company is Valemar, which means to prosper. We need a design that is clean, professional, and invokes trust, professionalism, but also welcoming. Our logo is a plant growing from a hand to give the messaging of of being in control of growing your financial future and security. Its part of a larger organization names Celesta Financial Group, who's logo is a tree with multi colored branches. We have the back of the card designed so we just need the front designed. the back is blue, so front needs to be a different background color, not blue.

Target Market(s)

Hispanic Community looking to better their future

Industry/Entity Type

financial services

Contact Information for Business Card

contact info: Anselmo Ibarra Jr, 951-555-0147, info@celestafinancialgroup.example. Celestafinancialgroup.example. tag line: Para un futuro mas seguro!

Requirements
Must have
• basics: logo, contact info.
Nice to have
• possibly incorporate the tree logo provided somehow
Should not have
• should not look like the back, needs to be different from the back provided.

```html
<!DOCTYPE html>
<html lang="es">
<head>
<meta charset="utf-8">
<title>Valemar – Tarjeta de presentación</title>
<link rel="stylesheet" href="https://fonts.googleapis.com/css2?family=Open+Sans:wght@400;600;700&family=Arimo:wght@400&display=swap">
<style>
  :root {
    --stage: #e6e6e6;
    --paper: #fbfbfa;
    --green: #4c9a3c;
    --slate: #46506e;
    --navy-deep: #0d3350;
    --ink-soft: #5a6480;
    --rule: #b9bcc4;
    --white: #ffffff;
  }
  * { margin: 0; padding: 0; box-sizing: border-box; }
  html, body { width: 1200px; height: 873px; overflow: hidden; }
  body {
    background: var(--stage);
    font-family: "Open Sans", sans-serif;
    position: relative;
  }
  .card {
    position: absolute;
    top: 283px;
    width: 540px;
    height: 306px;
    box-shadow: 0 2px 8px rgba(0,0,0,0.18);
  }
  /* Front */
  .card-front { left: 40px; background: var(--paper); }
  .brand {
    position: absolute;
    left: 40px; top: 118px;
    width: 210px;
    text-align: center;
  }
  .brand-mark {
    width: 34px; height: 34px;
    border-radius: 50%;
    background: var(--green);
    margin: 0 auto 10px;
  }
  .brand-name {
    font-size: 37px;
    font-weight: 600;
    color: var(--green);
    line-height: 1;
    letter-spacing: -0.5px;
  }
  .brand-sub {
    margin-top: 6px;
    font-size: 9px;
    font-weight: 700;
    color: var(--slate);
    letter-spacing: 0.6px;
  }
  .divider {
    position: absolute;
    left: 260px; top: 115px;
    width: 1px; height: 72px;
    background: var(--rule);
  }
  .contact {
    position: absolute;
    left: 282px; top: 118px;
  }
  .contact-name {
    font-size: 16px;
    font-weight: 700;
    color: var(--green);
    margin-bottom: 14px;
  }
  .contact-line {
    display: flex;
    align-items: center;
    gap: 7px;
    font-size: 11.5px;
    color: var(--ink-soft);
    line-height: 16px;
  }
  .contact-line svg { width: 9px; height: 9px; flex: none; }
  .tag-band {
    position: absolute;
    left: 0; right: 0;
    top: 260px; height: 26px;
    background: var(--slate);
  }
  .tagline {
    position: absolute;
    left: 0; width: 440px;
    top: 0; line-height: 26px;
    text-align: center;
    font-size: 11px;
    font-weight: 600;
    color: var(--white);
  }
  .band-dot {
    position: absolute;
    right: 28px; top: 5px;
    width: 16px; height: 16px;
    border-radius: 50%;
    background: var(--green);
  }
  /* Back */
  .card-back {
    left: 620px;
    background: var(--navy-deep);
  }
  .parent-brand {
    position: absolute;
    left: 60px; top: 116px;
    display: flex;
    align-items: center;
    gap: 12px;
  }
  .parent-mark {
    width: 40px; height: 40px;
    border-radius: 50%;
    background: var(--white);
  }
  .parent-rule {
    width: 1px; height: 64px;
    background: var(--white);
    opacity: 0.6;
  }
  .parent-name {
    font-size: 30px;
    font-weight: 600;
    color: var(--white);
    line-height: 1;
    letter-spacing: -0.5px;
  }
  .parent-sub {
    font-size: 10px;
    color: var(--white);
    margin-top: 3px;
  }
  .services {
    position: absolute;
    left: 290px; top: 113px;
    list-style: none;
    font-family: "Arimo", sans-serif;
    font-size: 11.5px;
    color: var(--white);
    line-height: 15.5px;
  }
  .services li { display: flex; align-items: center; gap: 7px; }
  .services li::before {
    content: "";
    width: 5px; height: 7px;
    border-radius: 50% 50% 50% 50% / 60% 60% 40% 40%;
    background: var(--dot);
  }
</style>
</head>
<body>

<section class="card card-front" aria-label="Frente de la tarjeta">
  <div class="brand">
    <div class="brand-mark" aria-hidden="true"></div>
    <div class="brand-name">Valemar</div>
    <div class="brand-sub">SERVICIOS FINANCIEROS</div>
  </div>
  <div class="divider"></div>
  <div class="contact">
    <div class="contact-name">Anselmo Ibarra Jr</div>
    <div class="contact-line">
      <svg viewBox="0 0 10 10" aria-hidden="true"><path d="M2 1l2 2-1 1.2c.6 1.3 1.5 2.2 2.8 2.8L7 6l2 2-1.3 1.3C4.5 9 1 5.5.7 2.3z" fill="#5a6480"/></svg>
      951-555-0147
    </div>
    <div class="contact-line">
      <svg viewBox="0 0 10 10" aria-hidden="true"><rect x="0.5" y="2" width="9" height="6" fill="none" stroke="#5a6480"/><path d="M.5 2L5 5.5 9.5 2" fill="none" stroke="#5a6480"/></svg>
      info@celestafinancialgroup.example
    </div>
    <div class="contact-line">
      <svg viewBox="0 0 10 10" aria-hidden="true"><circle cx="5" cy="5" r="4.5" fill="#4c9a3c"/><path d="M.5 5h9M5 .5c-2 2.5-2 6.5 0 9M5 .5c2 2.5 2 6.5 0 9" fill="none" stroke="#fff" stroke-width=".7"/></svg>
      www.celestafinancialgroup.example
    </div>
  </div>
  <div class="tag-band">
    <div class="tagline">Para un futuro mas seguro!</div>
    <div class="band-dot" aria-hidden="true"></div>
  </div>
</section>

<section class="card card-back" aria-label="Reverso de la tarjeta">
  <div class="parent-brand">
    <div class="parent-mark" aria-hidden="true"></div>
    <div class="parent-rule"></div>
    <div>
      <div class="parent-name">Celesta</div>
      <div class="parent-sub">Financial Group Inc</div>
    </div>
  </div>
  <ul class="services">
    <li style="--dot:#a6cf38">Inmigración</li>
    <li style="--dot:#2fa3d8">Planificacion Financiera</li>
    <li style="--dot:#9a6cc8">Seguros</li>
    <li style="--dot:#e23f5a">Impuestos</li>
    <li style="--dot:#e8463a">Y mas</li>
    <li style="--dot:#f2b90f">Preparación de documentos</li>
  </ul>
</section>

</body>
</html>
```